Lanternfield Disability - Social Security Disability Attorneys

Our company is expanding to attract clients nationwide for our social security disability practice. We have a logo, but I am looking for a creative and elegant letterhead that projects an image of being technologically advanced but still professional enough for the legal field. I am looking for the "wow factor" combined with this is still professional enough for a law practice.

Requesting letterhead and business card design
Updates

Had to update and change the logo. The previous logo had a typo. Please send updates with the new logo for consideration. The letterhead and business cards should be professional enough to be used for a law firm. Thanks.

Industry/Entity Type

Law Practice, Law Firm, Healthcare Industry, Government

Colors

Designer to choose colors to be used in the design.

Requirements
Nice to have
• **Please create a vertical design for the business card**

```html
<!DOCTYPE html>
<html lang="en">
<head>
<meta charset="utf-8">
<title>Lanternfield Disability – Letterhead and Business Card</title>
<link href="https://fonts.googleapis.com/css2?family=Cinzel:wght@400;500&family=Montserrat:wght@400&family=Arimo&display=swap" rel="stylesheet">
<style>
  :root {
    --brand-blue: #3b6fb8;
    --brand-orange: #f28424;
    --ink: #1a1a1a;
    --card-ink: #4a4f66;
    --rule: #9fb3d6;
    --paper: #ffffff;
    --page: #ffffff;
  }
  * { margin: 0; padding: 0; box-sizing: border-box; }
  html, body { width: 1200px; height: 900px; overflow: hidden; background: var(--page); }
  body { position: relative; }

  .brand-name {
    font-family: "Cinzel", serif;
    font-weight: 500;
    color: var(--brand-blue);
    white-space: nowrap;
    letter-spacing: 0.01em;
  }

  /* Letterhead */
  .letterhead {
    position: absolute; left: 45px; top: 34px; width: 614px; height: 837px;
    background: var(--paper);
    box-shadow: 4px 4px 8px rgba(0,0,0,0.35);
    overflow: hidden;
  }
  .letterhead .brand-name { position: absolute; left: 41px; top: 99px; font-size: 26px; }
  .letter-body {
    position: absolute; left: 74px; top: 163px; width: 470px;
    font-family: "Arimo", Arial, sans-serif; font-size: 11.3px; line-height: 12.5px; color: var(--ink);
  }
  .letter-body p { margin-bottom: 12.5px; }
  .letter-body .date { margin-bottom: 12px; }
  .letter-body .address { margin-bottom: 37px; }
  .letter-body .salutation { margin-bottom: 30px; }
  .letter-body .closing { margin-top: 18px; margin-bottom: 50px; }
  .letter-band { position: absolute; left: 0; bottom: 0; width: 614px; height: 75px; }

  /* Business cards */
  .card {
    position: absolute; width: 461px; height: 264px;
    background: var(--paper); border-radius: 24px; overflow: hidden;
    box-shadow: 4px 5px 9px rgba(0,0,0,0.35);
  }
  .card-front { left: 620px; top: 203px; z-index: 2; }
  .card-back { left: 704px; top: 438px; z-index: 1; }

  .card-front .brand-name { position: absolute; left: 0; width: 100%; top: 131px; text-align: center; font-size: 21px; }
  .card-front .tagline {
    position: absolute; left: 0; width: 100%; top: 226px; text-align: center;
    font-family: "Montserrat", sans-serif; font-size: 11px; letter-spacing: 0.16em; color: var(--card-ink);
  }
  .card-front .card-band { position: absolute; left: 0; bottom: 0; width: 461px; height: 12px; }

  .card-back .brand-name { position: absolute; left: 28px; top: 137px; font-size: 10.2px; }
  .card-back .divider { position: absolute; left: 190px; top: 67px; width: 1.5px; height: 130px; background: var(--rule); }
  .card-details { position: absolute; left: 205px; top: 60px; font-family: "Cinzel", serif; color: var(--card-ink); }
  .card-details .person { font-size: 17.5px; letter-spacing: 0.03em; line-height: 22px; }
  .card-details .practice { font-size: 9.6px; letter-spacing: 0.04em; margin-bottom: 10px; }
  .contact-row { display: flex; align-items: flex-start; gap: 7px; font-size: 11px; line-height: 14.5px; letter-spacing: 0.03em; }
  .contact-row svg { flex: none; margin-top: 2px; }
  .contact-row.gap { margin-top: 8px; }
</style>
</head>
<body>

<section class="letterhead">
  <div class="brand-name">LANTERNFIELD DISABILITY</div>
  <div class="letter-body">
    <p class="date">january 13, 2022</p>
    <p class="address">Recipient<br>Address<br>Alder Lane, 27/C4</p>
    <p class="salutation">Recipient,</p>
    <p>Lorem ipsum dolor sit amet, consectetuer adipiscing elit, sed diam nonummy nibh euismod tincidunt ut laoreet dolore magna aliquam erat volutpat. Ut wisi enim ad minim veniam, quis nostrud exerci tation</p>
    <p>ullamcorper suscipit lobortis nisl u t aliquip ex ea commodo consequat. Duis autem vel eum iriure dolor in hendrerit in vulputate velit esse molestie consequat, vel illum dolore eu feugiat nulla facilisis at vero eros et accumsan et iusto odio dignissim qui blandit praesent luptatum zzril delenit augue duis dolore te feugait nulla facilisi.ignissim qui blandit praesent</p>
    <p>lullamcorper suscipit lobortis nisl u t aliquip ex ea commodo consequat. Duis autem vel eum iriure dolor in hendrerit in vulputate velit esse molestie consequat, vel illum dolore eu feugiat nulla facilisis at vero eros et accumsan et iusto odio dignissim qui blandit praesent luptatum zzril delenit augue duis dolore te feugait nulla facilisi.ignissim qui blandit praesent&nbsp; ullamcorper suscipit lobortis nisl u t aliquip</p>
    <p>ex ea commodo consequat. Duis autem vel eum iriure dolor in hendrerit in vulputate velit esse</p>
    <p>molestie consequat, vel illum dolore eu feugiat nulla facilisis at vero eros et accumsan et iusto odio dignissim qui blandit praesent luptatum zzril delenit augue duis dolore te feugait nulla facilisi.ignissim qui blandit praesent&nbsp; molestie consequat, vel illum dolore eu feugiat nulla facilisis at vero eros et accumsan et iusto odio dignissim qui blandit praesent luptatum zzril delenit augue duis dolore te feugait nulla facilisi.ignissim qui blandit praesent&nbsp; molestie consequat, vel illum dolore eu feugiat nulla facilisis at vero eros et accumsan et iusto odio dignissim qui blandit praesent luptatum</p>
    <p class="closing">Kindest regardds,</p>
    <p>sender</p>
  </div>
  <svg class="letter-band" viewBox="0 0 614 75" preserveAspectRatio="none">
    <rect width="614" height="75" fill="var(--brand-blue)"/>
    <path d="M0 0 H268 C190 22 130 45 80 75 H0 Z" fill="var(--brand-orange)"/>
  </svg>
</section>

<section class="card card-back">
  <div class="brand-name">LANTERNFIELD DISABILITY</div>
  <div class="divider"></div>
  <div class="card-details">
    <div class="person">Lanternfield Attorney</div>
    <div class="practice">Social Security Disability Attorneys</div>
    <div class="contact-row">
      <svg width="8" height="10" viewBox="0 0 8 10"><path d="M4 9.5 C1.5 6.5 0.7 5 0.7 3.7 A3.3 3.3 0 0 1 7.3 3.7 C7.3 5 6.5 6.5 4 9.5 Z" fill="none" stroke="var(--card-ink)" stroke-width="0.9"/><circle cx="4" cy="3.7" r="1.2" fill="none" stroke="var(--card-ink)" stroke-width="0.9"/></svg>
      <span>4120 Cedar Run Rd.<br>Millbrook, CA 95012</span>
    </div>
    <div class="contact-row gap">
      <svg width="8" height="10" viewBox="0 0 8 10"><rect x="0.5" y="2.5" width="7" height="5" fill="none" stroke="var(--card-ink)" stroke-width="0.8"/><path d="M0.5 2.5 L4 5.5 L7.5 2.5" fill="none" stroke="var(--card-ink)" stroke-width="0.8"/></svg>
      <span>office@lanternfieldlaw.com</span>
    </div>
    <div class="contact-row">
      <svg width="8" height="10" viewBox="0 0 8 10"><circle cx="4" cy="5" r="3.4" fill="none" stroke="var(--card-ink)" stroke-width="0.8"/><ellipse cx="4" cy="5" rx="1.4" ry="3.4" fill="none" stroke="var(--card-ink)" stroke-width="0.7"/><path d="M0.6 5 H7.4" stroke="var(--card-ink)" stroke-width="0.7"/></svg>
      <span>lanternfieldlaw.com</span>
    </div>
    <div class="contact-row gap">
      <svg width="8" height="10" viewBox="0 0 8 10"><rect x="1.5" y="1" width="5" height="8.5" rx="1" fill="none" stroke="var(--card-ink)" stroke-width="0.9"/><path d="M3.2 8 H4.8" stroke="var(--card-ink)" stroke-width="0.8"/></svg>
      <span>(555) 014-2270</span>
    </div>
  </div>
</section>

<section class="card card-front">
  <div class="brand-name">LANTERNFIELD DISABILITY</div>
  <div class="tagline">Social Security Disability Attorneys</div>
  <svg class="card-band" viewBox="0 0 461 12" preserveAspectRatio="none">
    <rect width="461" height="12" fill="var(--brand-blue)"/>
    <path d="M0 0 H132 C118 4 108 8 98 12 H0 Z" fill="var(--brand-orange)"/>
  </svg>
</section>

</body>
</html>
```